Brightpath Works Mobile RV Repair

We are looking for a logo and business cards for a new start up business. We will be doing Mobile RV Repair.
We are in Texas.
I don't have any designs at this point.

Contact Information for Business Card

Emphasis should be on the “Mobile RV Repair” and not so much the name “Brightpath Works”

Requirements
Nice to have
• I like the Mobile RV Repair to cover most of the backside of the card! Not sure on the colors, would like to see it in a few different colors!

```html
<!DOCTYPE html>
<html lang="en">
<head>
<meta charset="utf-8">
<title>Brightpath Works Mobile RV Repair – Business Cards</title>
<link rel="stylesheet" href="https://fonts.googleapis.com/css2?family=Exo+2:wght@500;700;800&display=swap">
<style>
  :root {
    --stage: #1c1c1c;
    --card: #141414;
    --card-edge: #262626;
    --orange: #f07a2a;
    --orange-deep: #e8621f;
    --silver: #dcdfe2;
    --white: #ffffff;
    --ink: #111111;
  }
  * { box-sizing: border-box; margin: 0; padding: 0; }
  html, body {
    width: 1200px; height: 1200px; overflow: hidden;
    background: var(--stage);
    font-family: "Exo 2", sans-serif;
  }
  .sheet {
    position: relative; width: 1200px; height: 1200px;
  }
  .card {
    position: absolute; left: 220px;
    width: 760px; height: 434px;
    border-radius: 22px;
    background: radial-gradient(ellipse at 50% 40%, #1d1d1d 0%, var(--card) 70%);
    box-shadow: 0 0 0 1px var(--card-edge), 0 20px 40px rgba(0,0,0,.55);
    overflow: hidden;
  }
  .card--back { top: 110px; }
  .card--front { top: 620px; }
  .wordmark {
    position: absolute; left: 0; right: 0;
    display: flex; align-items: center; justify-content: center; gap: 18px;
  }
  .card--back .wordmark { top: 150px; }
  .card--front .wordmark { top: 70px; }
  .wordmark__dot {
    width: 26px; height: 26px; border-radius: 50%;
    background: var(--orange);
    flex: none;
  }
  .wordmark__name {
    color: var(--white);
    font-weight: 800;
    font-size: 40px;
    line-height: 1.05;
    text-transform: uppercase;
    text-align: center;
    letter-spacing: 1px;
  }
  .name-band {
    position: absolute; left: 0; right: 0; top: 270px; height: 52px;
    background: linear-gradient(90deg, var(--orange-deep) 0%, var(--orange) 30%, #f6c9a8 55%, var(--silver) 78%, var(--white) 100%);
    display: flex; align-items: center; justify-content: center;
  }
  .name-band__name {
    color: var(--ink);
    font-weight: 800; font-size: 30px;
    letter-spacing: 2px; text-transform: uppercase;
    font-style: italic;
  }
  .contacts {
    position: absolute; left: 56px; right: 40px; top: 348px;
    display: flex; align-items: center; gap: 36px;
    color: var(--white); font-weight: 500; font-size: 22px;
  }
  .contacts__item { display: flex; align-items: center; gap: 10px; }
  .contacts__icon { width: 22px; height: 22px; flex: none; }
</style>
</head>
<body>
<main class="sheet">
  <section class="card card--back" aria-label="Card back">
    <div class="wordmark">
      <span class="wordmark__dot"></span>
      <span class="wordmark__name">Brightpath Works<br>Mobile RV Repair</span>
    </div>
  </section>

  <section class="card card--front" aria-label="Card front">
    <div class="wordmark">
      <span class="wordmark__dot"></span>
      <span class="wordmark__name">Brightpath Works<br>Mobile RV Repair</span>
    </div>
    <div class="name-band">
      <span class="name-band__name">Dale Marlow</span>
    </div>
    <div class="contacts">
      <span class="contacts__item">
        <svg class="contacts__icon" viewBox="0 0 24 24" aria-hidden="true">
          <path fill="#f07a2a" d="M6.6 10.8a15.1 15.1 0 0 0 6.6 6.6l2.2-2.2c.3-.3.7-.4 1-.2 1.1.4 2.3.6 3.6.6.6 0 1 .4 1 1V20c0 .6-.4 1-1 1C10.6 21 3 13.4 3 4c0-.6.4-1 1-1h3.5c.6 0 1 .4 1 1 0 1.3.2 2.5.6 3.6.1.3 0 .7-.2 1z"/>
        </svg>
        210-555-0148
      </span>
      <span class="contacts__item">
        <svg class="contacts__icon" viewBox="0 0 24 24" aria-hidden="true">
          <rect x="2" y="5" width="20" height="14" rx="1.5" fill="#f07a2a"/>
          <path d="M3 6l9 7 9-7" fill="none" stroke="#141414" stroke-width="1.8"/>
        </svg>
        hello@brightpathrv.example
      </span>
    </div>
  </section>
</main>
</body>
</html>
```